Letterhead

Can you please design me a letterhead that I can use electronically in word as a template. I have attached my business card as I would like the design to reflect this logo.

```html
<!DOCTYPE html>
<html lang="en">
<head>
<meta charset="utf-8">
<title>Marrowby Letterhead</title>
<link href="https://fonts.googleapis.com/css2?family=Open+Sans:wght@400;700&display=swap" rel="stylesheet">
<style>
  :root {
    --backdrop: #464646;
    --paper: #ffffff;
    --brand-red: #9a0000;
    --ink-black: #000000;
    --ink-dark: #222222;
    --ink-light: #ffffff;
  }
  html, body {
    margin: 0;
    padding: 0;
    width: 1200px;
    height: 1000px;
    overflow: hidden;
    background: var(--backdrop);
    font-family: "Open Sans", Arial, sans-serif;
  }
  .letterhead {
    position: absolute;
    left: 292px;
    top: 40px;
    width: 639px;
    height: 903px;
    background: var(--paper);
    box-shadow: 3px 3px 6px rgba(0,0,0,0.5);
  }
  .brand {
    position: absolute;
    left: 30px;
    top: 8px;
  }
  .brand-name {
    margin: 0;
    font-size: 52px;
    font-weight: 400;
    line-height: 1;
    color: var(--brand-red);
    letter-spacing: -0.5px;
  }
  .brand-tagline {
    margin: 6px 0 0 4px;
    font-size: 11px;
    color: var(--ink-dark);
  }
  .principal-tab {
    position: absolute;
    right: 0;
    top: 0;
    width: 258px;
    height: 44px;
    background: var(--brand-red);
  }
  .principal-tab-underline {
    position: absolute;
    right: 0;
    top: 44px;
    width: 235px;
    height: 8px;
    background: var(--ink-black);
  }
  .principal-details {
    position: absolute;
    left: 53px;
    top: 2px;
    margin: 0;
    font-size: 16px;
    font-weight: 700;
    line-height: 20px;
    color: var(--ink-light);
    text-transform: uppercase;
  }
  .footer-rule {
    position: absolute;
    left: 0;
    top: 859px;
    width: 546px;
    height: 10px;
    background: var(--ink-black);
  }
  .footer-band {
    position: absolute;
    left: 0;
    top: 869px;
    width: 639px;
    height: 34px;
    background: var(--brand-red);
    display: flex;
    align-items: center;
    padding-left: 77px;
    box-sizing: border-box;
    gap: 19px;
    font-size: 14px;
    font-weight: 700;
    color: var(--ink-light);
  }
</style>
</head>
<body>
  <div class="letterhead">
    <header class="brand">
      <p class="brand-name">marrowby</p>
      <p class="brand-tagline">Business Consultants Pty Ltd</p>
    </header>

    <div class="principal-tab">
      <p class="principal-details">Helena Maitland<br>Principal</p>
    </div>
    <div class="principal-tab-underline"></div>

    <div class="footer-rule"></div>
    <footer class="footer-band">
      <span class="contact-phone">Telephone: 0412 555 018</span>
      <span class="contact-email">Email: helena@marrowby.net.au</span>
      <span class="contact-acn">ACN: 048 215 936</span>
    </footer>
  </div>
</body>
</html>
```